Create a memorable Web Design for real estate branding

we are a Minnepolis brokerage and boutique housing specialist with over 27 years of experience in the Global furnished housing industry, servicing the Greater Los Angeles area. Specializing in “warm environments” we offer a customized approach to satisfying our guests and client’s needs by offering a wide array of options in highly desirable areas. Additionally, Lantern Dwelling Partners offers assistance and expertise to home buyers, sellers and investors.

Industry/Entity Type

Real Estate

Number of Pages Required

1 page

Font styles to use
Serif
Sans Serif
Decorative

```html
<!DOCTYPE html>
<html lang="en">
<head>
<meta charset="utf-8">
<title>Lantern Dwelling Partners — Real Estate</title>
<link href="https://fonts.googleapis.com/css2?family=Roboto:wght@400;500;700&family=Open+Sans:wght@400;600;700&display=swap" rel="stylesheet">
<style>
:root{
  --green:#6fb22a;
  --green-dark:#5a9a1c;
  --teal:#1fa589;
  --teal-light:#2bb497;
  --ink:#2b2b2b;
  --muted:#777;
  --line:#dcdcdc;
  --panel:#eeeeee;
  --dark:#1b1d1f;
  --dark-2:#141516;
  --white:#fff;
}
*{box-sizing:border-box;margin:0;padding:0}
html,body{width:1200px;height:2970px;overflow:hidden;background:var(--white)}
body{font-family:"Open Sans",Arial,sans-serif;color:var(--ink);position:relative}
.abs{position:absolute}
h2,h3,h4{font-family:"Roboto",Arial,sans-serif}

/* header */
.brand{left:96px;top:26px;width:300px}
.brand-name{font-family:"Roboto",Arial,sans-serif;font-weight:700;font-size:30px;line-height:34px;color:var(--teal)}
.brand-sub{font-family:"Roboto",Arial,sans-serif;font-weight:700;font-size:30px;line-height:34px;color:var(--teal)}
.call{left:668px;top:50px;font-size:13px;color:#444;display:flex;align-items:center;gap:10px}
.call strong{color:var(--green);font-size:16px;font-weight:600}
.search{left:905px;top:46px;width:200px;height:32px;border:1px solid var(--line);font-size:10px;color:#aaa;padding:9px 10px;letter-spacing:.5px}
.search svg{position:absolute;right:10px;top:10px}

.nav{left:0;top:120px;width:1200px;height:55px;background:#f4f4f4;border-top:1px solid #e4e4e4;border-bottom:1px solid #e4e4e4}
.nav ul{list-style:none;display:flex;position:absolute;left:96px;width:1010px;height:55px}
.nav li{flex:1;text-align:center;font-family:"Roboto",Arial,sans-serif;font-size:12px;font-weight:500;color:#333;line-height:53px;border-left:1px solid #e2e2e2}
.nav li:last-child{border-right:1px solid #e2e2e2}
.nav li.active{background:var(--white);color:var(--teal);border-bottom:3px solid var(--teal)}

/* hero */
.hero{left:0;top:175px;width:1200px;height:515px;background:linear-gradient(180deg,#2f6fc4 0%,#5d98dc 35%,#8fb4cf 60%,#5a6e4c 85%,#3f5a2e 100%)}
.hero-lead{left:0;top:385px;width:1200px;text-align:center;color:var(--white);font-family:"Roboto",Arial,sans-serif;font-size:24px;letter-spacing:1px;text-shadow:0 1px 4px rgba(0,0,0,.4)}
.hero-title{left:0;top:420px;width:1200px;text-align:center;color:var(--white);font-family:"Roboto",Arial,sans-serif;font-weight:700;font-size:50px;text-shadow:0 2px 6px rgba(0,0,0,.45)}
.dots{left:558px;top:508px;display:flex;gap:16px}
.dots span{width:15px;height:15px;border-radius:50%;border:2px solid var(--white)}
.dots span.on{background:var(--green)}
.hero-rule{left:0;top:686px;width:1200px;height:4px;background:var(--green)}
.find-tab{left:104px;top:650px;width:202px;height:40px;background:var(--green);color:var(--white);font-family:"Roboto",Arial,sans-serif;font-weight:700;font-size:14px;line-height:40px;padding-left:22px}

/* search panel */
.finder{left:0;top:690px;width:1200px;height:240px;background:var(--panel)}
.field{position:absolute;top:56px;width:238px}
.field label{display:block;font-size:10px;color:#444;margin-bottom:9px;letter-spacing:.2px}
.select{height:40px;background:var(--white);border:1px solid #ddd;font-size:10px;color:#aaa;padding:13px 10px;position:relative}
.select:after{content:"";position:absolute;right:30px;top:6px;width:1px;height:26px;background:#e3e3e3}
.select svg{position:absolute;right:10px;top:17px}
.range-label{left:98px;top:145px;font-size:10px;color:#444}
.range{left:104px;top:170px;width:632px;height:12px;background:var(--white);border:1px solid #ccc;border-radius:6px}
.range-fill{left:104px;top:170px;width:270px;height:12px;background:#666;border-radius:6px}
.knob{width:18px;height:18px;border-radius:50%;background:var(--teal);border:4px solid #d9efe9;top:167px}
.range-value{left:760px;top:166px;font-size:13px;color:var(--green);font-weight:600}
.btn{background:var(--green);color:var(--white);font-family:"Roboto",Arial,sans-serif;font-weight:700;text-align:center;border-bottom:3px solid var(--green-dark)}
.search-btn{left:862px;top:144px;width:240px;height:46px;font-size:12px;line-height:43px}

/* welcome */
.section-title{left:0;width:1200px;text-align:center;font-family:"Roboto",Arial,sans-serif;font-weight:500;font-size:26px;color:var(--ink)}
.lede{left:130px;width:940px;text-align:center;font-size:12px;line-height:27px;color:#555}
.service{position:absolute;top:1128px;width:290px;text-align:center}
.service .ring{width:104px;height:104px;margin:0 auto;border-radius:50%;border:3px solid var(--teal);display:flex;align-items:center;justify-content:center}
.service .disc{width:80px;height:80px;border-radius:50%;background:var(--teal);display:flex;align-items:center;justify-content:center}
.service h4{margin-top:22px;font-size:13px;font-weight:700;color:#222}
.service p{margin-top:10px;font-size:11px;line-height:22px;color:#666}
.service a{display:block;margin-top:12px;font-size:10px;font-weight:700;color:var(--teal);text-decoration:none}
.connector{top:1180px;height:2px;border-top:2px dotted #ccc}
.connector:before,.connector:after{content:"";position:absolute;top:-6px;width:9px;height:9px;border-radius:50%;border:1px solid #ccc;background:var(--white)}
.connector:before{left:-5px}.connector:after{right:-5px}

/* booking */
.booking{left:0;top:1390px;width:1200px;height:278px;background:linear-gradient(180deg,#2a2a2a,#161616)}
.booking h2{position:absolute;top:50px;width:1200px;text-align:center;color:var(--white);font-weight:400;font-size:25px}
.booking p{position:absolute;top:92px;left:140px;width:920px;text-align:center;color:#bbb;font-size:11px;line-height:27px}
.email{left:268px;top:166px;width:500px;height:44px;background:var(--white);font-size:11px;color:#888;padding:14px 12px 0 38px}
.email svg{position:absolute;left:14px;top:15px}
.book-btn{left:776px;top:166px;width:156px;height:44px;font-size:12px;line-height:42px}

/* featured */
.card{position:absolute;top:1773px;width:314px;height:382px;background:var(--white);border:1px solid #e6e6e6;box-shadow:0 10px 14px -10px rgba(0,0,0,.25)}
.card .photo{position:absolute;left:4px;top:4px;width:304px;height:206px}
.card .sale{position:absolute;right:4px;top:42px;width:66px;height:30px;background:var(--green);color:var(--white);font-size:12px;line-height:30px;text-align:center}
.card .price{position:absolute;right:4px;top:74px;width:92px;height:34px;background:var(--teal);color:var(--white);font-size:15px;font-weight:600;line-height:34px;text-align:center}
.card h4{position:absolute;top:230px;width:100%;text-align:center;font-size:13px;font-weight:700;color:#222}
.card p{position:absolute;top:256px;left:30px;width:254px;text-align:center;font-size:11px;line-height:24px;color:#666}
.card .more{position:absolute;left:108px;top:314px;width:98px;height:36px;font-size:10px;line-height:33px}

/* boutique */
.boutique{left:0;top:2208px;width:1200px;height:377px;background:linear-gradient(180deg,#1fa286,#1d9c80 70%,#22a98b)}
.boutique h2{position:absolute;top:46px;width:1200px;text-align:center;color:var(--white);font-weight:500;font-size:25px}
.tile{position:absolute;top:104px;width:251px;height:182px}
.tile-cap{position:absolute;top:302px;width:251px;text-align:center;color:var(--white);font-size:12px;font-weight:600}
.tile-overlay{position:absolute;inset:0;background:rgba(111,178,42,.55);display:flex;align-items:center;justify-content:center}
.plus{width:40px;height:40px;border-radius:50%;background:var(--white);display:flex;align-items:center;justify-content:center}

/* partners */
.partners{left:0;top:2585px;width:1200px;height:90px;background:var(--white)}
.badge{position:absolute;top:32px;height:22px;background:#c9c9c9;border-radius:3px}

/* footer */
.footer{left:0;top:2675px;width:1200px;height:295px;background:var(--dark)}
.footer h4{position:absolute;top:30px;color:var(--white);font-size:14px;font-weight:500}
.links{position:absolute;left:98px;top:64px;list-style:none}
.links li{font-size:11px;color:#ccc;line-height:21px}
.contact{position:absolute;left:250px;top:66px;list-style:none}
.contact li{display:flex;gap:14px;font-size:11px;color:#ccc;line-height:20px;margin-bottom:18px}
.contact svg{flex:none;margin-top:4px}
.inquiry-text{position:absolute;left:582px;top:64px;width:210px;font-size:11px;line-height:22px;color:#888}
.inquiry-btn{left:582px;top:156px;width:174px;height:42px;font-size:12px;line-height:39px}
.articles{position:absolute;left:896px;top:66px;list-style:none}
.articles li{position:relative;padding-left:14px;margin-bottom:24px;font-size:11px;color:#ccc;line-height:20px}
.articles li:before{content:"";position:absolute;left:0;top:8px;width:5px;height:5px;border-radius:50%;background:#ccc}
.articles em{display:block;color:var(--green);font-size:10px}
.footer-bar{left:0;top:2920px;width:1200px;height:50px;background:var(--dark-2);border-top:1px solid #2a2a2a}
.copy{position:absolute;left:98px;top:17px;font-size:11px;color:#bbb}
.follow{position:absolute;left:880px;top:12px;display:flex;align-items:center;gap:9px;font-size:11px;color:#bbb}
.follow span.dot{width:24px;height:24px;border-radius:50%;border:1px solid #888}
</style>
</head>
<body>

<!-- header -->
<div class="abs brand">
  <div class="brand-name">Lantern Dwelling</div>
  <div class="brand-sub">Partners</div>
</div>
<div class="abs call">
  <svg width="18" height="18" viewBox="0 0 24 24"><path fill="#6fb22a" d="M6.6 10.8a15.1 15.1 0 0 0 6.6 6.6l2.2-2.2a1 1 0 0 1 1-.25 11.4 11.4 0 0 0 3.6.57 1 1 0 0 1 1 1V20a1 1 0 0 1-1 1A17 17 0 0 1 3 4a1 1 0 0 1 1-1h3.5a1 1 0 0 1 1 1c0 1.25.2 2.45.57 3.57a1 1 0 0 1-.25 1z"/></svg>
  <span>Call Now : <strong>(+100) 555-0142</strong></span>
</div>
<div class="abs search">SEARCH ....
  <svg width="11" height="11" viewBox="0 0 12 12"><circle cx="5" cy="5" r="3.6" fill="none" stroke="#6fb22a" stroke-width="1.6"/><line x1="7.6" y1="7.6" x2="11" y2="11" stroke="#6fb22a" stroke-width="1.6"/></svg>
</div>

<nav class="abs nav">
  <ul>
    <li class="active">HOME</li><li>ABOUT</li><li>SERVICES</li><li>PROPETIES</li><li>AGENTS</li><li>BLOG</li><li>CONTACT</li>
  </ul>
</nav>

<!-- hero -->
<div class="abs hero" role="img" aria-label="Photo of a downtown skyline with tall towers and palm trees under a blue sky"></div>
<div class="abs hero-lead">SPECIALIZING IN</div>
<div class="abs hero-title">“WARM ENVIRONMENTS”</div>
<div class="abs dots"><span class="on"></span><span></span><span></span></div>
<div class="abs hero-rule"></div>
<div class="abs find-tab">FIND YOUR PROPERTY</div>

<!-- property finder -->
<section class="abs finder">
  <div class="field" style="left:98px"><label>MAX OF BEDROOMS</label><div class="select">Any<svg width="8" height="5" viewBox="0 0 8 5"><path d="M0 0h8L4 5z" fill="#999"/></svg></div></div>
  <div class="field" style="left:352px"><label>MAX OF BATHROOMS</label><div class="select">Any<svg width="8" height="5" viewBox="0 0 8 5"><path d="M0 0h8L4 5z" fill="#999"/></svg></div></div>
  <div class="field" style="left:608px"><label>MIN AREA (Sqft)</label><div class="select">Any<svg width="8" height="5" viewBox="0 0 8 5"><path d="M0 0h8L4 5z" fill="#999"/></svg></div></div>
  <div class="field" style="left:862px"><label>MAX AREA (Sqft)</label><div class="select">Any<svg width="8" height="5" viewBox="0 0 8 5"><path d="M0 0h8L4 5z" fill="#999"/></svg></div></div>
  <div class="abs range-label">PRICING RANGE</div>
</section>
<div class="abs range" style="top:860px"></div>
<div class="abs range-fill" style="top:860px"></div>
<div class="abs knob" style="left:97px;top:857px"></div>
<div class="abs knob" style="left:726px;top:857px"></div>
<div class="abs range-value" style="top:856px">$0 - $10,000,00</div>
<div class="abs btn search-btn" style="top:834px">CLICK TO SEARCH HERE</div>

<!-- welcome -->
<h2 class="abs section-title" style="top:972px">WELCOME TO LANTERN DWELLING PARTNERS</h2>
<p class="abs lede" style="top:1016px">Sed ut perspiciatis unde omnis iste natus error sit voluptatem accusantium doloremque laudantium, totam rem aperiam, eaque ipsa quae ab illo inventore veritatis et quasi architecto beatae vitae dicta sunt explicabo. Nemo enim ipsam voluptatem quia voluptas sit aspernatur aut odit aut fugit, sed quia consequuntur magni dolores eos qui ratione voluptatem sequi nesciunt. Neque porro quisquam est, qui dolorem ipsum quia dolor sit amet, consectetur.</p>

<div class="abs connector" style="left:318px;width:212px"></div>
<div class="abs connector" style="left:672px;width:210px"></div>

<div class="service" style="left:101px">
  <div class="ring"><div class="disc"><svg width="40" height="36" viewBox="0 0 40 36"><path d="M20 2 2 18h5v16h10V24h6v10h10V18h5z" fill="#fff"/></svg></div></div>
  <h4>REAL ESTATE</h4>
  <p>Neque porro quisquam est, qui dolorem ipsum quiaersa dolor numquam eius modi tempora....</p>
  <a>READ MORE &#10230;</a>
</div>
<div class="service" style="left:455px">
  <div class="ring"><div class="disc"><svg width="34" height="40" viewBox="0 0 34 40"><path d="M11 2h12l-4 7h-4z" fill="#fff"/><path d="M15 10h4C28 14 33 24 31 32c-1 5-6 6-14 6S4 37 3 32C1 24 6 14 15 10z" fill="#fff"/><text x="17" y="32" text-anchor="middle" font-family="Roboto,Arial,sans-serif" font-weight="700" font-size="17" fill="#1fa589">$</text></svg></div></div>
  <h4>BROKERAGE</h4>
  <p>Neque porro quisquam est, qui dolorem ipsum quiaersa dolor numquam eius modi tempora....</p>
  <a>READ MORE &#10230;</a>
</div>
<div class="service" style="left:811px">
  <div class="ring"><div class="disc"><svg width="40" height="40" viewBox="0 0 40 40"><path d="M22 4h14v14L18 36 4 22z" fill="#fff"/><circle cx="29" cy="11" r="3" fill="#1fa589"/></svg></div></div>
  <h4>BOUTIQUE HOUSING</h4>
  <p>Neque porro quisquam est, qui dolorem ipsum quiaersa dolor numquam eius modi tempora....</p>
  <a>READ MORE &#10230;</a>
</div>

<!-- booking -->
<section class="abs booking" role="img" aria-label="Dark tinted photo of city buildings behind the booking form">
  <h2>Book Your House</h2>
  <p>Accusantium doloremque laudantium, totam rem aperiam, eaque ipsa quae ab illo inventore veritatis et quasi architecto beatae vitae dicta sunt explicabo. Nemo enim ipsam voluptatem quia voluptas sit aspernatur aut odit aut fugit, sed quia consequuntur magni dolores</p>
</section>
<div class="abs email" style="top:1556px">
  <svg width="12" height="12" viewBox="0 0 12 12"><path d="M0 5 12 0 7 12 5.5 6.5z" fill="#999"/></svg>
  Enter Your e-mail Address
</div>
<div class="abs btn book-btn" style="top:1556px">BOOK NOW TODAY!</div>

<!-- featured properties -->
<h2 class="abs section-title" style="top:1712px">FEATURED PROPERTIES</h2>

<article class="card" style="left:100px">
  <div class="photo" role="img" aria-label="Photo of a white two-storey family house with a green lawn" style="background:linear-gradient(180deg,#8db3d9 0%,#d8dfe4 40%,#6f8f4a 75%,#4f7a2c 100%)"></div>
  <div class="sale">SALE!</div><div class="price">$129,000</div>
  <h4>PROPERTY NAME</h4>
  <p>Duis aute irure dolor in reprehenderit in voluptate dolore eu fugiat nulla pariatur...</p>
  <div class="btn more">READ MORE</div>
</article>
<article class="card" style="left:443px">
  <div class="photo" role="img" aria-label="Photo of a grey suburban house with trees and a wide lawn" style="background:linear-gradient(180deg,#6a9a45 0%,#8c9a9e 40%,#6b7a55 65%,#4e8b2a 100%)"></div>
  <div class="sale">SALE!</div><div class="price">$129,000</div>
  <h4>PROPERTY NAME</h4>
  <p>Duis aute irure dolor in reprehenderit in voluptate dolore eu fugiat nulla pariatur...</p>
  <div class="btn more">READ MORE</div>
</article>
<article class="card" style="left:786px">
  <div class="photo" role="img" aria-label="Photo of a modern white villa with palm trees" style="background:linear-gradient(180deg,#3f78c6 0%,#9fbde0 40%,#d7dbdc 60%,#5f8a3c 100%)"></div>
  <div class="sale">SALE!</div><div class="price">$129,000</div>
  <h4>PROPERTY NAME</h4>
  <p>Duis aute irure dolor in reprehenderit in voluptate dolore eu fugiat nulla pariatur...</p>
  <div class="btn more">READ MORE</div>
</article>

<!-- boutique housing -->
<section class="abs boutique">
  <h2>BOUTIQUE HOUSING</h2>
  <div class="tile" style="left:98px;background:linear-gradient(180deg,#7ea1c2,#8d8f7a 55%,#5d8a33)" role="img" aria-label="Photo of a large family house">
    <div class="tile-overlay"><div class="plus"><svg width="16" height="16" viewBox="0 0 16 16"><path d="M7 1h2v6h6v2H9v6H7V9H1V7h6z" fill="#6fb22a"/></svg></div></div>
  </div>
  <div class="tile" style="left:349px;background:linear-gradient(180deg,#3b74c9,#a9c3e0 40%,#e3e3e0 65%,#9a9a96)" role="img" aria-label="Photo of a modern white house with a driveway"></div>
  <div class="tile" style="left:600px;background:linear-gradient(180deg,#a9c6e6,#7d8c88 45%,#5e8d3a 80%,#4f7f2b)" role="img" aria-label="Photo of a grey two-storey house with a lawn"></div>
  <div class="tile" style="left:851px;background:linear-gradient(180deg,#3270c8,#7a9cc4 40%,#6f7f8a 65%,#5a8a36)" role="img" aria-label="Photo of a blue-grey house with white trim"></div>
  <div class="tile-cap" style="left:98px">Accusantium Doloremqu</div>
  <div class="tile-cap" style="left:349px">Accusantium Doloremqu</div>
  <div class="tile-cap" style="left:600px">Accusantium Doloremqu</div>
  <div class="tile-cap" style="left:851px">Accusantium Doloremqu</div>
</section>

<!-- partners -->
<section class="abs partners" aria-label="Partners">
  <div class="badge" style="left:120px;width:92px"></div>
  <div class="badge" style="left:268px;width:88px"></div>
  <div class="badge" style="left:410px;width:60px;top:24px;height:38px"></div>
  <div class="badge" style="left:516px;width:96px"></div>
  <div class="badge" style="left:680px;width:80px;top:26px;height:34px"></div>
  <div class="badge" style="left:798px;width:100px"></div>
  <div class="badge" style="left:968px;width:92px"></div>
</section>

<!-- footer -->
<footer class="abs footer">
  <h4 style="left:98px">LINKS</h4>
  <ul class="links"><li>Home</li><li>About</li><li>Services</li><li>Propeties</li><li>Agents</li><li>Blog</li><li>Contact</li></ul>

  <h4 style="left:250px">CONTACT US</h4>
  <ul class="contact">
    <li><svg width="10" height="13" viewBox="0 0 10 13"><path d="M5 0a5 5 0 0 1 5 5c0 3.5-5 8-5 8S0 8.5 0 5a5 5 0 0 1 5-5z" fill="#ccc"/><circle cx="5" cy="5" r="1.8" fill="#1b1d1f"/></svg><span>420 Harbor Light Ave.,<br>Suite 210, Lakeview, MN. 55400</span></li>
    <li><svg width="11" height="11" viewBox="0 0 24 24"><path fill="#ccc" d="M6.6 10.8a15.1 15.1 0 0 0 6.6 6.6l2.2-2.2a1 1 0 0 1 1-.25 11.4 11.4 0 0 0 3.6.57 1 1 0 0 1 1 1V20a1 1 0 0 1-1 1A17 17 0 0 1 3 4a1 1 0 0 1 1-1h3.5a1 1 0 0 1 1 1c0 1.25.2 2.45.57 3.57a1 1 0 0 1-.25 1z"/></svg><span>Phone: 800-555-0137</span></li>
    <li><svg width="12" height="11" viewBox="0 0 12 11"><rect x="2" y="0" width="8" height="3" fill="#ccc"/><rect x="0" y="3" width="12" height="6" rx="1" fill="#ccc"/><rect x="3" y="7" width="6" height="4" fill="#ccc"/></svg><span>Fax: 612-555-0198</span></li>
    <li><svg width="12" height="9" viewBox="0 0 12 9"><rect width="12" height="9" fill="#ccc"/><path d="M0 0l6 5 6-5" fill="none" stroke="#1b1d1f" stroke-width="1.2"/></svg><span>Email: hello@lanterndwelling.example</span></li>
  </ul>

  <h4 style="left:582px">INQUIRY HERE</h4>
  <p class="inquiry-text">Sed ut perspiciatis unde omnis isteera natus error sit voluptatem accusanties doloremque la udantium.ipsum dolo .totam rem aperiam, eaque</p>
  <div class="abs btn inquiry-btn" style="top:156px">CLICK INQUIRY HERE &nbsp;&#8250;</div>

  <h4 style="left:896px">LATEST ARTICLES</h4>
  <ul class="articles">
    <li>Sed ut perspiciatis unde<em>Published May 30, 2016 at 11:06 pm</em></li>
    <li>Sed ut perspiciatis unde<em>Published May 30, 2016 at 11:06 pm</em></li>
  </ul>
</footer>
<div class="abs footer-bar">
  <div class="copy">Copyright © 2016 &nbsp;Lantern Dwelling Partners | Allrights Reserved.</div>
  <div class="follow">Follow With Us: <span class="dot"></span><span class="dot"></span><span class="dot"></span><span class="dot"></span></div>
</div>

</body>
</html>
```